Real Estate Marketing Postcards need a fresh look, Front & Back

I have a current postcard design (attached) that lacks design quality and too much use of color. I do like the basic color scheme, but I'm open to anything that cleans up the look and incorporates space for the existing text. I'm not opposed to a design with a white background, more white space. The design should be full bleed according to the attached specs. I would like this to be sent over in an Adobe format, something like InDesign.

The company logo will remain the same colors and appearance. The headshot will likely be updated in the coming weeks.

I am attaching a sample of a recent card plus a template from the printer showing the back of the card and location of the address and postage section that must remain blank. I am also including the logo and another logo designed for use with a white (or non blue) background.

(feel free to swap in stock photos of whatever house you want, but the front of the card should incorporate at least one photo of a house.)

Target Market(s)

Home owners.

Industry/Entity Type

Real Estate

Font styles to use
Sans Serif

Colors

Designer to choose colors to be used in the design.

Requirements
Must have
• Company logo, the headshot, the contact info on the back, a photo or photos of a house along with the text "Just Sold" or "Sold" featured on the front of the card.

```html
<!DOCTYPE html>
<html lang="en">
<head>
<meta charset="utf-8">
<title>Hillside Realtor Postcard – Front &amp; Back</title>
<link href="https://fonts.googleapis.com/css2?family=Lato:wght@400;700;900&family=Bebas+Neue&display=swap" rel="stylesheet">
<style>
  :root {
    --navy: #1a5b94;
    --navy-text: #1d5a96;
    --sky: #a9dbf6;
    --header-text: #d9effc;
    --paper: #ffffff;
    --mailing-area: #f4f5f7;
    --canvas: #e9ebee;
    --photo-sky: #a8cfee;
    --photo-wall: #eceadf;
    --photo-roof: #5e6266;
    --photo-green: #5f8f3e;
    --portrait-top: #b9b4c4;
    --portrait-bottom: #d9d6de;
    --badge: #8a8d91;
  }
  * { box-sizing: border-box; margin: 0; padding: 0; }
  html, body { width: 967px; height: 1200px; overflow: hidden; }
  body {
    background: var(--canvas);
    font-family: "Lato", Arial, sans-serif;
    position: relative;
  }
  .postcard {
    position: absolute;
    left: 126px;
    width: 892px;
    height: 630px;
    transform: scale(0.8);
    transform-origin: top left;
    background: var(--paper);
    overflow: hidden;
  }
  .postcard--front { top: 85px; }
  .postcard--back { top: 610px; }
  .shapes { position: absolute; inset: 0; width: 892px; height: 630px; }

  /* Front */
  .house-photo {
    position: absolute; left: 0; top: 0; width: 892px; height: 454px;
    background: linear-gradient(180deg,
      var(--photo-sky) 0%, #cfe4f4 28%,
      var(--photo-roof) 40%, var(--photo-roof) 52%,
      var(--photo-wall) 58%, var(--photo-wall) 66%,
      #3c3029 72%, #3c3029 86%,
      var(--photo-green) 94%, var(--photo-green) 100%);
  }
  .headline {
    position: absolute; left: 0; top: 20px; width: 892px; height: 99px;
    display: flex; align-items: center; justify-content: center;
    color: var(--header-text); font-weight: 700; font-size: 57px; letter-spacing: -0.5px;
  }
  .agent-portrait {
    position: absolute; border: 2px solid var(--navy);
    background: linear-gradient(180deg, var(--portrait-top), var(--portrait-bottom));
  }
  .agent-portrait--front { left: 30px; top: 441px; width: 174px; height: 173px; }
  .brand-title {
    position: absolute; right: 37px; top: 489px;
    font-family: "Bebas Neue", Impact, sans-serif; font-weight: 400;
    font-size: 88px; line-height: 1; color: var(--navy); letter-spacing: 0.5px;
    white-space: nowrap;
  }
  .tagline {
    position: absolute; right: 37px; top: 580px; height: 26px;
    display: flex; align-items: center;
    color: #fff; font-weight: 700; font-size: 19px; letter-spacing: 0.3px;
  }

  /* Back */
  .selling-title {
    position: absolute; left: 28px; top: 36px; width: 326px; text-align: center;
    font-weight: 900; font-size: 76px; line-height: 1; color: var(--navy); letter-spacing: -1px;
  }
  .selling-copy {
    position: absolute; left: 30px; top: 122px; width: 322px; text-align: center;
    color: var(--navy-text); font-weight: 400; font-size: 17px; line-height: 21px;
  }
  .selling-copy p + p { margin-top: 21px; }
  .reasons-copy {
    position: absolute; left: 405px; top: 35px; width: 252px;
    color: #fff; font-size: 17px; line-height: 21px;
  }
  .reasons-copy p + p { margin-top: 21px; }
  .brokerage-mark {
    position: absolute; left: 686px; top: 38px; width: 180px; height: 128px;
    display: flex; flex-direction: column; align-items: center; justify-content: center; gap: 8px;
    color: #fff; font-weight: 700; font-size: 20px; line-height: 1.1; text-align: center;
  }
  .brokerage-mark__square { width: 16px; height: 16px; background: #fff; }
  .brokerage-phone { margin-top: 6px; font-size: 21px; }
  .badge {
    position: absolute; top: 180px; width: 46px; height: 48px;
    background: var(--badge); border: 2px solid #c9cbce;
  }
  .badge--first { left: 756px; }
  .badge--second { left: 816px; }
  .agent-portrait--back {
    left: 405px; top: 247px; width: 174px; height: 174px; border: 3px solid #fff;
  }
  .agent-card {
    position: absolute; left: 591px; top: 252px;
    color: var(--navy-text); font-weight: 400; font-size: 17px; line-height: 21px;
  }
  .agent-card__name { font-size: 31px; font-weight: 900; line-height: 34px; color: var(--navy); }
  .agent-card__nickname { font-size: 19px; font-weight: 700; line-height: 22px; margin-bottom: 5px; color: var(--navy); }
  .disclaimer {
    position: absolute; left: 382px; top: 431px; width: 510px; text-align: center;
    font-size: 9.5px; color: #1f3f5c;
  }
</style>
</head>
<body>

<section class="postcard postcard--front" aria-label="Postcard front">
  <div class="house-photo" role="img" aria-label="Photo of a white two-storey house with a dark roof and a glass sunroom, garden in front"></div>
  <svg class="shapes" viewBox="0 0 892 630" aria-hidden="true">
    <rect x="0" y="20" width="892" height="99" fill="var(--navy)"/>
    <rect x="0" y="454" width="892" height="176" fill="var(--paper)"/>
    <polygon points="0,399 312,399 298,466 0,466" fill="var(--navy)"/>
    <polygon points="310,471 892,471 892,630 265,630" fill="var(--sky)"/>
    <polygon points="562,580 892,580 892,606 545,606" fill="var(--navy)"/>
  </svg>
  <h1 class="headline">Another home JUST LISTED by</h1>
  <div class="agent-portrait agent-portrait--front" role="img" aria-label="Agent headshot"></div>
  <h2 class="brand-title">The Hillside Realtor</h2>
  <p class="tagline">You KNOW it won’t last long!</p>
</section>

<section class="postcard postcard--back" aria-label="Postcard back">
  <svg class="shapes" viewBox="0 0 892 630" aria-hidden="true">
    <polygon points="360,21 892,21 892,231 382,231" fill="var(--navy)"/>
    <polygon points="382,233 892,233 892,446 360,446" fill="var(--sky)"/>
    <rect x="0" y="446" width="892" height="184" fill="var(--mailing-area)"/>
  </svg>

  <h2 class="selling-title">SELLING?</h2>
  <div class="selling-copy">
    <p>Chossing the right agent is critical to your success.</p>
    <p>Your home is your biggest assest.</p>
    <p>you own it to yourself to have every advantage by choosing the local agent with the expertise to position your hillside home and get is sold fast and for top dollar.</p>
    <p>There is no other agent who knows the hillside market better. Contact me today to get your home SOLD</p>
  </div>

  <div class="reasons-copy">
    <p>There are 3 key reasons a home doesn’t sell, and #1 is chossing the wrong agent to market your property.</p>
    <p>Contatct me today to discuss your home’s value and what steps I will take to assures your success.</p>
  </div>

  <div class="brokerage-mark">
    <span class="brokerage-mark__square"></span>
    <span>Willow Run<br>Real Estate</span>
    <span class="brokerage-phone">(301) 555-0140</span>
  </div>
  <div class="badge badge--first" aria-hidden="true"></div>
  <div class="badge badge--second" aria-hidden="true"></div>

  <div class="agent-portrait agent-portrait--back" role="img" aria-label="Agent headshot"></div>
  <div class="agent-card">
    <p class="agent-card__name">Marco Bellandi</p>
    <p class="agent-card__nickname">“The Hillside Realtor”</p>
    <p>Principal Broker, REALTOR</p>
    <p>Willow Run Real Estate</p>
    <p>(301) 555-0140 Office</p>
    <p>(301) 555-0172 Cell</p>
    <p>www.hillsidehomeguide.com</p>
  </div>
  <p class="disclaimer">if your home is currently listed with another broker, this is not intended as a solicitation of that listing</p>
</section>

</body>
</html>
```